Velvette by Marisa Holt business cards

I am after a business card that will fit the name of my business - velvette.
I want something classy and sexy and nothing tacky.
Ideas that I like are Zebra print backgrounds glitter back grounds
Two ideas I had were
1. Zebra print in black and white, the name Velvette by Marisa Holt and a shilouette of a woman laying on top of the name. Or instead of zebra a glitter background.
2. Idea very similar except for instead of a woman a pair of lips maybe a hot pink glitter or a gold glitter depending on background with the business name between the lips.
Or you can do something completely different.

Industry/Entity Type

Business

```html
<!DOCTYPE html>
<html lang="en">
<head>
<meta charset="utf-8">
<title>Velvette by Marisa Holt – Business Cards</title>
<link rel="stylesheet" href="https://fonts.googleapis.com/css2?family=Montserrat:wght@300&family=Dancing+Script:wght@400&display=swap">
<style>
  :root {
    --backdrop: #e8e2d8;
    --card-black: #050505;
    --stripe-light: #f2f2f2;
    --stripe-mid: #b9b9b9;
    --hot-pink: #ec1c8c;
    --ink-white: #f5f5f5;
  }
  html, body {
    margin: 0;
    padding: 0;
    width: 1200px;
    height: 1000px;
    overflow: hidden;
    background: var(--backdrop);
  }
  .stage {
    position: relative;
    width: 1200px;
    height: 1000px;
  }
  .card {
    position: absolute;
    width: 700px;
    height: 400px;
    background: var(--card-black);
    overflow: hidden;
    box-shadow: 0 6px 18px rgba(0,0,0,0.25);
  }
  .card--front { left: 90px; top: 70px; }
  .card--back  { left: 410px; top: 530px; }
  .zebra-band {
    position: absolute;
    left: 0;
    top: 0;
    width: 700px;
    height: 400px;
  }
  .brand-name {
    position: absolute;
    left: 56px;
    bottom: 70px;
    margin: 0;
    font-family: "Montserrat", sans-serif;
    font-weight: 300;
    font-size: 40px;
    letter-spacing: 1px;
    color: var(--ink-white);
  }
  .holder {
    position: absolute;
    right: 48px;
    top: 150px;
    text-align: right;
  }
  .holder-name {
    margin: 0;
    font-family: "Dancing Script", cursive;
    font-size: 58px;
    line-height: 1;
    color: var(--hot-pink);
  }
  .holder-title {
    margin: 6px 0 0;
    font-family: "Dancing Script", cursive;
    font-size: 30px;
    color: var(--ink-white);
  }
  .contact-list {
    position: absolute;
    left: 48px;
    bottom: 36px;
    margin: 0;
    padding: 0;
    list-style: none;
    font-family: "Dancing Script", cursive;
    font-size: 24px;
    line-height: 1.35;
  }
  .contact-label { color: var(--hot-pink); }
  .contact-value { color: var(--ink-white); }
</style>
</head>
<body>
<main class="stage">

  <section class="card card--front">
    <svg class="zebra-band" viewBox="0 0 700 400" role="img" aria-label="Black and white zebra print band across the top of the card">
      <defs>
        <linearGradient id="zebra-front" x1="0" y1="0" x2="1" y2="1">
          <stop offset="0" stop-color="var(--stripe-light)"/>
          <stop offset="0.5" stop-color="var(--stripe-mid)"/>
          <stop offset="1" stop-color="var(--stripe-light)"/>
        </linearGradient>
      </defs>
      <polygon points="0,0 700,0 700,250 430,130 0,95" fill="url(#zebra-front)"/>
    </svg>
    <h1 class="brand-name">Velvette by Marisa Holt</h1>
  </section>

  <section class="card card--back">
    <svg class="zebra-band" viewBox="0 0 700 400" role="img" aria-label="Black and white zebra print band in the top left corner">
      <defs>
        <linearGradient id="zebra-back" x1="0" y1="0" x2="1" y2="1">
          <stop offset="0" stop-color="var(--stripe-light)"/>
          <stop offset="0.55" stop-color="var(--stripe-mid)"/>
          <stop offset="1" stop-color="var(--stripe-light)"/>
        </linearGradient>
      </defs>
      <polygon points="0,0 480,0 280,150 0,175" fill="url(#zebra-back)"/>
    </svg>
    <div class="holder">
      <h2 class="holder-name">Marisa Holt</h2>
      <p class="holder-title">Director</p>
    </div>
    <ul class="contact-list">
      <li><span class="contact-label">Phone:</span> <span class="contact-value">555 010 248</span></li>
      <li><span class="contact-label">Email:</span> <span class="contact-value">marisaholt@velvette.com</span></li>
      <li><span class="contact-label">Website:</span> <span class="contact-value">velvettebymarisaholt.com</span></li>
    </ul>
  </section>

</main>
</body>
</html>
```